The Timber Loft

We need a business card design for our wardrobe company.
Please visit our website www.zorvelcabinets.com to get an idea of who we are.

```html
<!DOCTYPE html>
<html lang="en">
<head>
<meta charset="utf-8">
<title>The Timber Loft — Business Card</title>
<link href="https://fonts.googleapis.com/css2?family=Montserrat:wght@500;600&family=Arimo:wght@400;700&display=swap" rel="stylesheet">
<style>
  :root {
    --stage: #e4e6e8;
    --card: #ffffff;
    --ink: #1c1c1c;
    --ink-soft: #333333;
    --rule: #3a3a3a;
    --shadow: rgba(0, 0, 0, 0.18);
  }
  * { box-sizing: border-box; margin: 0; padding: 0; }
  html, body {
    width: 1200px;
    height: 785px;
    overflow: hidden;
    background: var(--stage);
  }
  .canvas {
    position: relative;
    width: 1200px;
    height: 785px;
  }
  .card {
    position: absolute;
    width: 520px;
    height: 297px;
    background: var(--card);
    border-radius: 26px;
    box-shadow: 0 10px 28px var(--shadow);
    color: var(--ink);
  }
  .card--front { left: 50px; top: 110px; }
  .card--back  { left: 630px; top: 378px; }

  /* Brand lockup */
  .brand {
    display: flex;
    align-items: center;
    gap: 16px;
  }
  .brand__mark {
    width: 64px;
    height: 64px;
    background: var(--ink);
    flex-shrink: 0;
  }
  .brand__name {
    font-family: "Montserrat", sans-serif;
    font-weight: 600;
    font-size: 19px;
    letter-spacing: 0.3px;
    text-transform: uppercase;
    color: var(--ink);
    line-height: 1.2;
    white-space: nowrap;
  }
  .brand__tagline {
    font-family: "Montserrat", sans-serif;
    font-weight: 500;
    font-size: 15px;
    color: var(--ink);
    margin-top: 6px;
    padding-left: 24px;
    white-space: nowrap;
  }
  .card--front .brand {
    position: absolute;
    left: 60px;
    top: 50%;
    transform: translateY(-50%);
  }

  /* Back side */
  .card__divider {
    position: absolute;
    left: 282px;
    top: 42px;
    width: 1.5px;
    height: 210px;
    background: var(--rule);
  }
  .person {
    position: absolute;
    left: 44px;
    top: 58px;
    font-family: "Arimo", sans-serif;
    font-weight: 700;
    color: var(--ink);
  }
  .person__name { font-size: 25px; line-height: 1.1; }
  .person__role { font-size: 22px; line-height: 1.1; padding-left: 34px; text-transform: lowercase; }

  .contacts {
    position: absolute;
    left: 44px;
    top: 150px;
    list-style: none;
    font-family: "Arimo", sans-serif;
    font-size: 16px;
    color: var(--ink-soft);
  }
  .contacts__item {
    display: flex;
    align-items: center;
    gap: 18px;
    height: 26px;
    white-space: nowrap;
  }
  .contacts__icon {
    width: 14px;
    height: 14px;
    fill: var(--ink);
    flex-shrink: 0;
  }
  .card--back .brand {
    position: absolute;
    left: 300px;
    top: 108px;
    gap: 10px;
  }
  .card--back .brand__mark { width: 38px; height: 38px; }
  .card--back .brand__name { font-size: 11.5px; }
  .card--back .brand__tagline { font-size: 9.5px; margin-top: 3px; padding-left: 12px; }
</style>
</head>
<body>
<main class="canvas">

  <section class="card card--front" aria-label="Business card front">
    <div class="brand">
      <span class="brand__mark" aria-hidden="true"></span>
      <div>
        <p class="brand__name">The Timber Loft</p>
        <p class="brand__tagline">Built Square, Made True</p>
      </div>
    </div>
  </section>

  <section class="card card--back" aria-label="Business card back">
    <div class="person">
      <p class="person__name">Marla Quint</p>
      <p class="person__role">ceo</p>
    </div>

    <ul class="contacts">
      <li class="contacts__item">
        <svg class="contacts__icon" viewBox="0 0 24 24" aria-hidden="true"><path d="M6.6 10.8c1.4 2.8 3.8 5.1 6.6 6.6l2.2-2.2c.3-.3.7-.4 1-.2 1.1.4 2.3.6 3.6.6.6 0 1 .4 1 1V20c0 .6-.4 1-1 1C10.6 21 3 13.4 3 4c0-.6.4-1 1-1h3.5c.6 0 1 .4 1 1 0 1.300.2 2.5.6 3.6.1.3 0 .7-.2 1z"/></svg>
        <span>555 014 2287</span>
      </li>
      <li class="contacts__item">
        <svg class="contacts__icon" viewBox="0 0 24 24" aria-hidden="true"><path d="M7 3h10v5H7zM4 9h16a2 2 0 0 1 2 2v6h-4v4H6v-4H2v-6a2 2 0 0 1 2-2zm4 7v3h8v-3z"/></svg>
        <span>555 014 2290</span>
      </li>
      <li class="contacts__item">
        <svg class="contacts__icon" viewBox="0 0 24 24" aria-hidden="true"><path d="M2 5h20v14H2zm2 2v.5l8 5 8-5V7l-8 5z"/></svg>
        <span>hello@zorvelcabinets.com</span>
      </li>
      <li class="contacts__item">
        <svg class="contacts__icon" viewBox="0 0 24 24" aria-hidden="true"><path d="M12 2a10 10 0 1 0 0 20 10 10 0 0 0 0-20zm6.9 6h-3a15 15 0 0 0-1.4-3.9A8 8 0 0 1 18.9 8zM12 4c.8 1.2 1.5 2.5 1.9 4h-3.8c.4-1.5 1.1-2.8 1.9-4zM4.3 14a8 8 0 0 1 0-4h3.4a16 16 0 0 0 0 4zm.8 2h3a15 15 0 0 0 1.4 3.9A8 8 0 0 1 5.1 16zm3-8h-3a8 8 0 0 1 4.4-3.9A15 15 0 0 0 8.1 8zM12 20c-.8-1.2-1.5-2.5-1.9-4h3.8c-.4 1.5-1.1 2.8-1.9 4zm2.3-6H9.7a14 14 0 0 1 0-4h4.6a14 14 0 0 1 0 4zm.2 5.9c.6-1.2 1.1-2.5 1.4-3.9h3a8 8 0 0 1-4.4 3.9zm1.8-5.9a16 16 0 0 0 0-4h3.4a8 8 0 0 1 0 4z"/></svg>
        <span>www.zorvelcabinets.com</span>
      </li>
    </ul>

    <span class="card__divider" aria-hidden="true"></span>

    <div class="brand">
      <span class="brand__mark" aria-hidden="true"></span>
      <div>
        <p class="brand__name">The Timber Loft</p>
        <p class="brand__tagline">Built Square, Made True</p>
      </div>
    </div>
  </section>

</main>
</body>
</html>
```